Meridian Handsets business card design

I would like to see some designs for a business card for Meridian Handsets. I would like the business card to be double sided. It will need to have a similar colour / look and feel to our website www.meridianhandsets.com.au I have also attached our latest flyer. Final designs to be handed over in Photoshop format so that I can edit the business card when needed please.

Industry/Entity Type

Business

Contact Information for Business Card

Gavin Thornley
sales@meridianhandsets.com.au
Business Development Manager
ph: (08) 6197 5821
www.meridianhandsets.com.au

Font styles to use
Serif
Sans Serif

Requirements
Must have
• If you could please utilise our colour scheme as seen on our website and the attached flyer.
• I would also like the final design to be in a Photoshop format so that I can edit it when needed please.

```html
<!DOCTYPE html>
<html lang="en">
<head>
<meta charset="utf-8">
<title>Meridian Handsets – Business Card</title>
<link rel="stylesheet" href="https://fonts.googleapis.com/css2?family=Lato:ital,wght@0,400;0,700;1,300&family=Montserrat:wght@500&display=swap">
<style>
  :root {
    --stage: #2b2b2b;
    --card: #f7f7f7;
    --brand-blue: #1b87c9;
    --ink: #333333;
    --ink-dark: #1a1a1a;
    --white: #ffffff;
  }
  * { box-sizing: border-box; margin: 0; padding: 0; }
  html, body {
    width: 1200px; height: 997px; overflow: hidden;
    background: var(--stage);
    font-family: "Lato", sans-serif;
  }
  .canvas { position: relative; width: 1200px; height: 997px; }

  .card {
    position: absolute;
    width: 640px; height: 366px;
    background: var(--card);
    border-radius: 24px;
    overflow: hidden;
    box-shadow: 0 12px 30px rgba(0,0,0,.45);
  }
  .card--back { left: 60px; top: 70px; }
  .card--front { left: 500px; top: 560px; }

  .wordmark {
    position: absolute;
    font-family: "Montserrat", sans-serif;
    font-weight: 500;
    font-size: 46px;
    color: var(--ink);
    white-space: nowrap;
    letter-spacing: .3px;
  }
  .card--back .wordmark { left: 70px; top: 150px; }
  .card--front .wordmark { left: 150px; top: 150px; }

  .band {
    position: absolute; top: 0; bottom: 0;
    width: 68px;
    background: var(--brand-blue);
  }
  .band--right { right: 0; }
  .band--left { left: 0; }
  .band__text {
    position: absolute; left: 50%; top: 50%;
    white-space: nowrap; color: var(--white);
  }
  .band--right .band__text {
    transform: translate(-50%, -50%) rotate(90deg);
    font-style: italic; font-weight: 300; font-size: 17px; letter-spacing: .5px;
  }
  .band--left .band__text {
    transform: translate(-50%, -50%) rotate(-90deg);
    font-size: 22px; letter-spacing: .3px;
  }

  .tab {
    position: absolute; right: -8px; top: 22px;
    width: 20px; height: 40px;
    border-radius: 8px;
    background: var(--brand-blue);
  }

  .person { position: absolute; right: 34px; top: 26px; text-align: right; }
  .person__name { color: var(--brand-blue); font-weight: 700; font-size: 18px; letter-spacing: .5px; }
  .person__title { color: var(--ink-dark); font-size: 14px; }

  .contacts { position: absolute; left: 100px; bottom: 40px; list-style: none; }
  .contacts li {
    display: flex; align-items: center; gap: 14px;
    color: var(--brand-blue); font-size: 18px; margin-top: 14px;
  }
  .contacts svg { width: 16px; height: 16px; flex: none; }
</style>
</head>
<body>
<main class="canvas">

  <section class="card card--back" aria-label="Card back">
    <div class="wordmark">Meridian Handsets</div>
    <div class="band band--right">
      <span class="band__text">Phone systems for your business</span>
    </div>
  </section>

  <section class="card card--front" aria-label="Card front">
    <div class="band band--left">
      <span class="band__text">www.meridianhandsets.com</span>
    </div>
    <div class="tab"></div>
    <div class="person">
      <p class="person__name">GAVIN THORNLEY</p>
      <p class="person__title">Business Development Manager</p>
    </div>
    <div class="wordmark">Meridian Handsets</div>
    <ul class="contacts">
      <li>
        <svg viewBox="0 0 16 16" aria-hidden="true"><rect x="4" y="1" width="8" height="14" rx="1.5" fill="none" stroke="#333" stroke-width="1.4"/><line x1="7" y1="12.5" x2="9" y2="12.5" stroke="#333" stroke-width="1.2"/></svg>
        <span>(08) 6197 5821</span>
      </li>
      <li>
        <svg viewBox="0 0 16 16" aria-hidden="true"><rect x="1" y="3" width="14" height="10" fill="#333"/><polyline points="1,3 8,9 15,3" fill="none" stroke="#f7f7f7" stroke-width="1.2"/></svg>
        <span>sales@meridianhandsets.com.au</span>
      </li>
    </ul>
  </section>

</main>
</body>
</html>
```